Mrs Tidwell

I would like an A5 size two sided flyer designed. This flyer is for handing out and pinningon notice boards. The brochure is prodominately for a male audience and I would prefer that it is not too 'busy'.

My business is complete housekeeping business targeted at fly in fly out miners in WA Australia. The business designs customised packages for the individual or household and completing all work while the person is at work. It is about making life simple for them so when they come home on their break all of the chores are completed and they don't have to do anything. Payments are made by Direct debit on a weekly or fortninghtly basis.

I am looking for bookings to start early 2013 for all areas of Perth.

10% discount on servcies if they included in a package with a regular house clean.

I would not like to see my exact wording from here just put into a design I would like the designer to add some thought to the design..

Please see below a list of my services.

House Cleaning
Regular clean
Spring clean
End of lease or moving clean

Inside
Linen washed
Clothes washed
Clothes ironed
Breakfast basket (Continental)
Breakfast basket (Deluxe)
Dishwashing/drying
Wheelie bins put out and in
Wheelie bins cleaned
Mail collected
Drinks stacked in fridge
Garage cleaned
Windows cleaned
Fridge Cleaned
Oven cleaned
Cupboards cleaned and organised
Carpets steam cleaned
Plants watered

Outside
Lawns mowed
Edges trimmed
Extra garden services
Windows washed
Cobwebs removed
Gutters cleaned
Reticulation maintenance/repairs
Patio area cleaned
Lawn and garden fertilising
Rubbish removal

Other
Alcohol delivery
Meet tradesperson/suppliers
Grocery shopping+
Run errands+
Bills paid+
Send or collect parcels+
Dry cleaning dropped off+
Clothing repairs alterations
Present shopping wrapping, card selection+

Your car
Car washed and vacuumed
Car detailed
Car drop off and collected for service and/or repairs+

Prodominately males and Miners

Shopping

```html
<!DOCTYPE html>
<html lang="en">
<head>
<meta charset="utf-8">
<title>Mrs Tidwell – Complete Housekeeping Services</title>
<link rel="stylesheet" href="https://fonts.googleapis.com/css2?family=Montserrat:wght@400&family=Kaushan+Script&display=swap">
<style>
  :root {
    --red: #e31e26;
    --maroon: #4d0710;
    --ink: #111111;
    --note: #3a0a0e;
    --paper: #ffffff;
    --edge: #9a9a9a;
    --script: "Kaushan Script", cursive;
    --sans: "Montserrat", Arial, sans-serif;
  }
  html, body {
    margin: 0;
    width: 1200px;
    height: 851px;
    overflow: hidden;
    background: var(--paper);
  }
  .flyer {
    position: relative;
    width: 1200px;
    height: 851px;
    overflow: hidden;
    font-family: var(--sans);
  }
  .flyer-shapes { position: absolute; left: 0; top: 0; }
  .brand-name {
    position: absolute; left: 48px; top: 100px; margin: 0;
    font-family: var(--sans); font-weight: 400; font-size: 36px;
    line-height: 44px; color: var(--ink);
  }
  .brand-tagline {
    position: absolute; left: 48px; top: 154px; margin: 0;
    font-family: var(--script); font-size: 18px; color: var(--ink);
  }
  .headline {
    position: absolute; left: 866px; top: 36px; width: 310px; margin: 0;
    font-family: var(--script); font-weight: 400; font-size: 52px; line-height: 59px;
    color: var(--ink); text-align: center;
  }
  .cleaning-list {
    position: absolute; left: 895px; top: 222px;
    margin: 0; padding: 0; list-style: none;
    color: var(--paper); font-size: 23px; line-height: 25.5px; letter-spacing: 1.2px;
  }
  .service-group { position: absolute; color: var(--paper); }
  .service-group h2 {
    font-family: var(--script); font-weight: 400; font-size: 26px;
    line-height: 28px; margin: 0;
  }
  .service-group ul {
    list-style: none; margin: 0; padding: 0;
    font-size: 17.5px; line-height: 20px; letter-spacing: 1.2px;
  }
  .service-group .more {
    margin: 0; font-family: var(--script); font-size: 19px; line-height: 24px;
  }
  .service-group .more-small { font-size: 16px; }
  .group-inside { left: 36px; top: 420px; }
  .group-outside { left: 279px; top: 420px; }
  .group-other { left: 522px; top: 420px; }
  .group-car { left: 522px; top: 645px; }
  .rates {
    position: absolute; left: 900px; top: 570px; width: 300px; margin: 0;
    font-family: var(--script); font-size: 42px; line-height: 50px;
    color: var(--ink); text-align: center;
  }
  .rates-note {
    position: absolute; left: 745px; top: 738px; width: 460px; margin: 0;
    font-size: 14.5px; line-height: 19px; color: var(--note); text-align: center;
  }
  .contact-web {
    position: absolute; left: 25px; top: 790px;
    font-size: 17px; line-height: 27px; color: var(--ink);
  }
  .contact-phone {
    position: absolute; left: 440px; top: 784px; margin: 0;
    font-size: 37px; line-height: 46px; color: var(--ink);
  }
</style>
</head>
<body>
<main class="flyer">
  <svg class="flyer-shapes" width="1200" height="851" viewBox="0 0 873 617" preserveAspectRatio="none" aria-hidden="true">
    <defs>
      <linearGradient id="curl-right" x1="0" y1="0" x2="1" y2="0">
        <stop offset="0" stop-color="#4d0710"/>
        <stop offset="1" stop-color="#e31e26"/>
      </linearGradient>
      <linearGradient id="curl-bottom" x1="0" y1="0" x2="1" y2="0">
        <stop offset="0" stop-color="#e31e26"/>
        <stop offset="1" stop-color="#4d0710"/>
      </linearGradient>
      <linearGradient id="sweep-low" x1="0" y1="1" x2="1" y2="0">
        <stop offset="0" stop-color="#4d0710"/>
        <stop offset="0.7" stop-color="#8a0e18"/>
        <stop offset="1" stop-color="#e31e26"/>
      </linearGradient>
    </defs>
    <rect class="red-field" x="10" y="22" width="843" height="593" fill="#e31e26"/>
    <path class="curl-right" d="M598,22 L660,22 C640,140 615,260 570,350 C605,250 615,130 598,22 Z" fill="url(#curl-right)"/>
    <path class="curl-bottom" d="M150,238 C320,250 470,290 570,350 C470,318 320,282 150,238 Z" fill="url(#curl-bottom)"/>
    <path class="sweep-low" d="M455,526 C560,470 640,380 700,318 C690,360 620,440 455,526 Z" fill="url(#sweep-low)"/>
    <path class="page" d="M1,24 Q300,4 600,22 C615,130 605,250 570,350 C470,285 300,238 10,236 L1,232 Z" fill="#ffffff" stroke="#9a9a9a" stroke-width="0.8"/>
  </svg>

  <p class="brand-name">Mrs Tidwell</p>
  <p class="brand-tagline">Home chores done while you're away on site</p>

  <h1 class="headline">Complete housekeeping Services</h1>
  <ul class="cleaning-list">
    <li>House Cleaning</li>
    <li>Regular clean</li>
    <li>Spring clean</li>
    <li>End of lease or</li>
    <li>moving clean</li>
  </ul>

  <section class="service-group group-inside">
    <h2>Inside</h2>
    <ul>
      <li>Linen washed</li>
      <li>Clothes washed</li>
      <li>Breakfast basket</li>
      <li>Dishwashing/drying</li>
      <li>Mail collected</li>
      <li>Complete cleaning</li>
      <li>Cupboards cleaned</li>
      <li>Carpets cleaned</li>
      <li>Plants watered</li>
    </ul>
    <p class="more">and more...</p>
  </section>

  <section class="service-group group-outside">
    <h2>Outside</h2>
    <ul>
      <li>Lawns mowed</li>
      <li>Edges trimmed</li>
      <li>Gardens</li>
      <li>Windows washed</li>
      <li>Cobwebs removed</li>
      <li>Gutters cleaned</li>
      <li>Patio area cleaned</li>
      <li>Rubbish removal</li>
    </ul>
    <p class="more">and more...</p>
  </section>

  <section class="service-group group-other">
    <h2>Other</h2>
    <ul>
      <li>Alcohol delivery</li>
      <li>Grocery shopping+</li>
      <li>Run errands+</li>
      <li>Bills paid+</li>
      <li>Send or collect parcels+</li>
      <li>Dry cleaning dropped off+</li>
      <li>Clothing repairs alterations</li>
    </ul>
    <p class="more more-small">and more...</p>
  </section>

  <section class="service-group group-car">
    <h2>Your car</h2>
    <ul>
      <li>Car washed</li>
      <li>vacuumed</li>
    </ul>
  </section>

  <p class="rates">We do<br>Great rates<br>on packages</p>
  <p class="rates-note">We offer a great discount on package deals,<br>call us for details.</p>

  <div class="contact-web">
    <div>enquiries@mrstidwell.com.au</div>
    <div>www.mrstidwell.com.au</div>
  </div>
  <p class="contact-phone">Call 08 61234567 or 0412345678</p>
</main>
</body>
</html>
```